Tessaro Lane Website

We are starting a marketing company and to do that we need a website! We want a website that will inspire and persuade to bring out the awesomeness in our clients.
What we want to see:
- Inspirational and persuasive imagery that relate to Branding.
- No cliche images eg. business man, suits and hand shakes
- We want to transform and educate our clients.
- We want to show them the path and would like our website to really act as a guide that guides them step by step through our process.
- We want the portray that we are an investment but not have a pretentious way to it. We put our heart into every project and that is how we treat our clients.
-When you submit your design please include what platform you have created for. Preference would be Wordpress or Joobla.

We have included the psd file for the wire frame, logo files, font files, site map and a link to a video we create to give you more information on what we would like to see. http://clipvault-demo.example/t/qx903LmaP

Feel free to make small modification to the logos if you think it will improve it. Your creativity and advice is most welcome.

One thing we forgot. We would like to have our contact information near the top of the website as well as at the bottom.  Here is out contact info:

Email: info@tessarolane.ca
Phone: 555-013-4829

Reason: As we are new with the platform and that we want to optimize our results, we decided to extend the deadline by 15 days. Thanks!

Target Market(s)

28-60, Male and Female, Oil field, Local Businesses, Dentists, Chiropractors, Hair salon, Construction/Renovation, Events etc

Industry/Entity Type

Investment

Requirements
Must have
• - 4 Inspirational and persuasive Imagery for the top portion of the website
- Must have a feel as if your not on a website an example of this is linked below.
http://www.pitchgallery-demo.example/design/482907/web-design-by-dalia-fenwick
Nice to have
• - Creative advice from you.
- Creative buttons for Get Free Quote and Subscribe buttons. Something out of the box that draws peoples attention. eg. a 'B' button. Just and example but still something related to branding.
Should not have
• No Cliches

```html
<!DOCTYPE html>
<html lang="en">
<head>
<meta charset="utf-8">
<title>Tessaro Lane</title>
<link href="https://fonts.googleapis.com/css2?family=Lilita+One&family=Great+Vibes&family=Carlito:ital,wght@0,400;0,700;1,400;1,700&family=Open+Sans:ital,wght@0,400;0,700;1,700&display=swap" rel="stylesheet">
<style>
:root{
  --page:#e6e6e6;
  --panel:#efefef;
  --card:#f5f5f5;
  --green:#5f9a1e;
  --green-light:#9fd13a;
  --ink:#1d1d1d;
  --grey-dark:#3a3a3a;
  --icon:#555555;
  --footer:#2b2b2b;
  --white:#ffffff;
}
*{margin:0;padding:0;box-sizing:border-box}
html,body{width:1200px;height:982px;overflow:hidden}
body{background:var(--page);position:relative;font-family:"Carlito","Open Sans",sans-serif;color:var(--ink)}
.site{position:absolute;left:63px;top:0;width:1073px;height:848px;background:var(--panel)}
.header-side{position:absolute;left:63px;top:0;width:262px;height:349px;
  background:
    radial-gradient(ellipse 140px 120px at 220px 300px,rgba(240,230,225,.9),transparent 70%),
    linear-gradient(180deg,#f7f7f8 0%,#eef0f2 40%,#d6d0cf 72%,#b9a7a5 100%)}
.header-photo{position:absolute;left:325px;top:0;width:811px;height:349px;
  background:
    radial-gradient(ellipse 160px 200px at 90px 230px,rgba(245,238,225,.95),transparent 75%),
    radial-gradient(ellipse 220px 140px at 380px 90px,rgba(175,185,150,.8),transparent 75%),
    radial-gradient(ellipse 260px 200px at 640px 200px,rgba(140,160,95,.85),transparent 75%),
    linear-gradient(135deg,#d8d0c8 0%,#b4b596 30%,#93a567 60%,#a9b08a 100%)}
.tab-strip{position:absolute;left:333px;top:16px;width:795px;height:39px;background:rgba(255,255,255,.2)}
.tab{position:absolute;top:22px;font-family:"Lilita One",sans-serif;font-size:21px;letter-spacing:.5px;color:rgba(90,90,90,.7)}
.tab.active{color:var(--white);text-shadow:0 1px 2px rgba(0,0,0,.4)}
.brand{position:absolute;left:70px;top:32px;display:flex;align-items:center;gap:10px}
.brand-mark{width:44px;height:44px;background:var(--grey-dark);border-radius:6px}
.brand-name{font-family:"Carlito",sans-serif;font-weight:700;font-size:31px;color:var(--grey-dark);line-height:1}
.tagline{position:absolute;left:102px;top:94px;font-style:italic;font-weight:700;font-size:15px;color:#333}
.header-contact{position:absolute;left:76px;top:119px;font-size:12.5px;font-weight:700;color:#4a4a4a}
.header-contact span+span::before{content:"·";margin:0 6px}
.main-nav{position:absolute;left:88px;top:148px;list-style:none}
.main-nav li{font-family:"Lilita One",sans-serif;font-size:23px;letter-spacing:1.5px;color:var(--green);
  height:39.3px;text-shadow:0 1px 0 #fff,0 2px 3px rgba(0,0,0,.35)}
.band{position:absolute;left:50px;top:332px;width:1099px;height:73px}
.welcome{position:absolute;left:460px;top:352px;font-family:"Great Vibes",cursive;font-size:35px;color:var(--white);text-shadow:0 1px 2px rgba(0,0,0,.35)}
.tips{position:absolute;left:936px;top:351px;font-family:"Lilita One",sans-serif;color:var(--white);text-shadow:0 1px 2px rgba(0,0,0,.5)}
.tips .big{font-size:23.5px;line-height:1}
.tips .small{font-size:15px;line-height:1.25;letter-spacing:.2px}
.connect-ribbon{position:absolute;left:91px;top:379px;width:163px;height:107px}
.connect-label{position:absolute;left:105px;top:412px;width:80px;text-align:center;font-family:"Open Sans",sans-serif;font-style:italic;font-weight:700;line-height:1.05;font-size:15px}
.connect-label .a{color:var(--white)}
.connect-label .b{color:var(--green-light)}
.social-box{position:absolute;left:71px;top:496px;width:181px;height:113px;border-radius:10px;
  background:linear-gradient(180deg,#f8f8f8,#dcdcdc);border:1px solid #cfcfcf;box-shadow:inset 0 1px 0 #fff}
.social-icons{position:absolute;left:0;top:0;pointer-events:none}
.content-card{position:absolute;left:264px;top:424px;width:648px;height:394px;background:var(--card);
  border:1px solid #dedede;box-shadow:0 0 3px rgba(0,0,0,.08)}
.card-brand{position:absolute;left:0;top:24px;width:100%;display:flex;justify-content:center;align-items:center;gap:10px}
.card-brand .brand-mark{width:40px;height:40px}
.card-brand .brand-name{font-size:29px}
.card-rule{position:absolute;left:10px;top:86px;width:626px;height:1px;background:linear-gradient(90deg,transparent,#d6d6d6 20%,#d6d6d6 80%,transparent)}
.card-text{position:absolute;left:8px;top:106px;width:625px;font-size:15.6px;line-height:21.8px;text-align:justify;color:var(--ink)}
.card-text p+p{margin-top:21.8px}
.card-text .lead{color:var(--green);font-style:italic;font-weight:700}
.quote-btn{position:absolute;left:486px;top:343px;width:149px;height:31px;border-radius:16px;
  background:linear-gradient(180deg,#fff,#eaeaea);box-shadow:0 1px 2px rgba(0,0,0,.15);
  font-family:"Open Sans",sans-serif;font-weight:700;font-size:13px;text-align:right;padding-right:10px;line-height:31px;color:#111}
.newsletter{position:absolute;left:945px;top:426px;width:180px}
.field{display:block;height:43px;margin-bottom:8px;border-radius:10px;border:2px solid #d0d0d0;
  background:linear-gradient(180deg,#fff,#e4e4e4);padding-left:14px;line-height:39px;
  font-family:"Open Sans",sans-serif;font-style:italic;font-weight:700;font-size:12.5px;color:#333}
.subscribe-btn{display:block;margin:4px 0 0 48px;width:93px;height:32px;border-radius:16px;
  background:linear-gradient(180deg,#6a6a6a,#1f1f1f);color:var(--white);text-align:center;line-height:32px;
  font-family:"Lilita One",sans-serif;font-size:15px;letter-spacing:.5px}
.footer{position:absolute;left:0;top:848px;width:1200px;height:134px;background:var(--footer);color:var(--white);font-family:Arial,"Open Sans",sans-serif}
.footer-nav{position:absolute;left:286px;top:26px;display:flex;list-style:none;font-size:13px}
.footer-nav li+li::before{content:"|";margin:0 20.5px}
.copyright{position:absolute;left:459px;top:52px;font-size:12px;letter-spacing:.3px}
</style>
</head>
<body>
<div class="site"></div>

<header>
  <div class="header-side" role="img" aria-label="Softly faded photo continuing behind the navigation"></div>
  <div class="header-photo" role="img" aria-label="Photo of a young man drawing a face on a fogged window"></div>
  <div class="tab-strip"></div>
  <span class="tab" style="left:357px">TESSARO LANE</span>
  <span class="tab active" style="left:596px">BE FOUND</span>
  <span class="tab" style="left:785px">CONNECT</span>
  <span class="tab" style="left:962px">GET GROWING</span>

  <div class="brand"><span class="brand-mark"></span><span class="brand-name">Tessaro Lane</span></div>
  <div class="tagline">Because You´re Awesome!</div>
  <div class="header-contact"><span>info@tessarolane.ca</span><span>555-013-4829</span></div>

  <ul class="main-nav">
    <li>STRATEGY</li><li>PORTFOLIO</li><li>ABOUT US</li><li>CONTACT US</li><li>BLOG</li>
  </ul>
</header>

<svg class="band" viewBox="0 0 1099 73" aria-hidden="true">
  <defs>
    <linearGradient id="bandGreen" x1="0" y1="0" x2="0" y2="1">
      <stop offset="0" stop-color="#a6d83f"/><stop offset="1" stop-color="#5e9a1c"/>
    </linearGradient>
  </defs>
  <path d="M0 18 Q0 0 14 0 L14 17 Z" fill="#7fb52a"/>
  <path d="M1099 18 Q1099 0 1085 0 L1085 17 Z" fill="#7fb52a"/>
  <rect x="0" y="17" width="1099" height="56" fill="url(#bandGreen)"/>
</svg>
<div class="welcome">Welcome Message</div>
<div class="tips"><div class="big">Get Tips &amp; Tricks!</div><div class="small">Subscribe to our Newsletter</div></div>

<svg class="connect-ribbon" viewBox="0 0 163 107" aria-hidden="true">
  <defs>
    <linearGradient id="ribbon" x1="0" y1="0" x2="0" y2="1">
      <stop offset="0" stop-color="#7a7a7a"/><stop offset="1" stop-color="#3b3b3b"/>
    </linearGradient>
  </defs>
  <path d="M108 0 Q150 0 163 20 L113 20 Z" fill="#1a1a1a"/>
  <path d="M0 10 Q0 0 12 0 L110 0 Q120 0 120 12 L120 86 L62 106 L0 86 Z" fill="url(#ribbon)"/>
  <path d="M22 82 L98 82 L60 96 Z" fill="#f2f2f2"/>
</svg>
<div class="connect-label"><div class="a">Get</div><div class="b">Connected</div></div>

<div class="social-box"></div>
<svg class="social-icons" width="1200" height="982" aria-hidden="true">
  <g fill="var(--icon)" stroke="#e8e8e8" stroke-width="2">
    <circle cx="103" cy="529" r="17"/>
    <circle cx="160" cy="529" r="17"/>
    <circle cx="219" cy="529" r="17"/>
    <circle cx="128" cy="576" r="17"/>
    <circle cx="187" cy="576" r="17"/>
  </g>
  <!-- globe -->
  <g fill="none" stroke="#fff" stroke-width="1.6">
    <circle cx="103" cy="529" r="8"/>
    <ellipse cx="103" cy="529" rx="3.5" ry="8"/>
    <path d="M95 529 H111"/>
  </g>
  <!-- speech bubble -->
  <path d="M152 522 H168 Q170 522 170 524 V533 Q170 535 168 535 H159 L154 539 V535 H152 Q150 535 150 533 V524 Q150 522 152 522 Z" fill="#fff"/>
  <!-- plus -->
  <path d="M219 520 V538 M210 529 H228" stroke="#fff" stroke-width="4"/>
  <!-- mail -->
  <rect x="118" y="569" width="20" height="14" fill="#fff"/>
  <path d="M118 569 L128 577 L138 569" fill="none" stroke="var(--icon)" stroke-width="1.5"/>
  <!-- location pin -->
  <path d="M187 586 C182 579 180 576 180 572 A7 7 0 0 1 194 572 C194 576 192 579 187 586 Z" fill="#fff"/>
  <circle cx="187" cy="572" r="2.5" fill="var(--icon)"/>
</svg>

<main class="content-card">
  <div class="card-brand"><span class="brand-mark"></span><span class="brand-name">Tessaro Lane</span></div>
  <div class="card-rule"></div>
  <div class="card-text">
    <p><span class="lead">Lorem Ipsum is simply dummy text of the printing and typesetting industry.</span> Lorem Ipsum has been the industry's standard dummy text ever since the 1500s, when an unknown printer took a galley of type and scrambled it to make a type specimen book. It has survived not only five centuries, but also the leap into electronic typesetting, remaining essentially unchanged. Contrary to popular belief, Lorem Ipsum is not simply random text. It has roots in a piece of classical Latin literature from 45 BC, making it over 2000 years old. Martin Ellery,</p>
    <p>It was popularised in the 1960s with the release of Setform sheets containing Lorem Ipsum passages, and more recently with desktop publishing software like Pagewright Studio including versions of Lorem Ipsum.Contrary to popular belief, Lorem Ipsum is not simply random text.</p>
  </div>
  <div class="quote-btn">Get a Free Quote!</div>
</main>

<form class="newsletter">
  <span class="field">Your Name</span>
  <span class="field">Your Email</span>
  <span class="subscribe-btn">Subscribe</span>
</form>

<footer class="footer">
  <ul class="footer-nav">
    <li>Site Map</li><li>Strategy</li><li>Portfolio</li><li>About Us</li><li>Contact Us</li><li>Blog</li>
  </ul>
  <div class="copyright">©TESSARO LANE INC. 2013</div>
</footer>
</body>
</html>
```